Nutritional Company Label and Box

Design for bottle label and box for nutritional supplement products. This will be a boilerplate for use on different vitamin product types. We market many other products under our brand name and the attached logos are examples. The name of our supplement line will be Torvesk Vitalorns, we want to use the attached logo of Torvesk and add the Vitalorns. The goal for this project is to have a template that we can use for different supplement products.

Target Market(s)

Health Products

Industry/Entity Type

Vitamin

Logo Text

Torvesk Vitalornsals

Font styles to use
Sans Serif

Colors

Designer to choose colors to be used in the design.

Requirements
Must have
• Vitalorns in the Logo can be a secondary more traditional font below the Torvesk Script and allow for small tagline
• On the label and box we want an area where we can insert the specific producdt name, for example, MCT OIL and small icon, this area would be interchangeable and we could insert, Multi Vitamin, Omega 3 Oil etc. within this main design. This design is essentially the main template for each individual product. Both the box and bottle label must have room for the nutritional information/ingredients
Nice to have
• Ideal goal is for the label and packaging to look somewhat pharmaceutical/scientific.
• We like the packaging for Pelmo Grovens supplements seen on Quorbix. https://www.quorbix-market.example/s?marketplaceID=QZRPLMNWT3BHY&me=B7KTRWQZN4LMPV&merchant=B7KTRWQZN4LMPV&redirect=true Also on box and label some type of badge showing 3 rd party approval. We like the color palettes used in the Pelmo Grovens packaging.

```html
<!DOCTYPE html>
<html lang="en">
<head>
<meta charset="utf-8">
<title>Torvesk Nutrition – Multi Vitamin Packaging</title>
<link rel="stylesheet" href="https://fonts.googleapis.com/css2?family=Montserrat:wght@400;500;600&family=Roboto+Condensed:wght@400;500&display=swap">
<style>
  :root {
    --backdrop: #c6c6c6;
    --paper: #f7f7f7;
    --green: #5c9f4a;
    --band: #3d7a33;
    --rule: #e9f1e6;
    --yellow: #f1b52b;
    --ink: #1e1e1e;
    --silver: #dcdcdc;
    --badge: #2a2a2a;
    --badge-ring: #e0a92a;
  }
  * { box-sizing: border-box; margin: 0; padding: 0; }
  html, body { width: 1200px; height: 1200px; overflow: hidden; }
  body {
    background: var(--backdrop);
    font-family: "Montserrat", sans-serif;
    position: relative;
  }

  .panel {
    position: absolute;
    background: var(--green);
    overflow: hidden;
    box-shadow: 0 6px 18px rgba(0,0,0,.12);
  }
  .box-front { left: 60px; top: 190px; width: 480px; height: 820px; }
  .bottle-label { left: 580px; top: 300px; width: 560px; height: 600px; }

  .panel__top {
    position: absolute; left: 0; right: 0; top: 0;
    background: var(--paper);
  }
  .box-front .panel__top { height: 350px; }
  .bottle-label .panel__top { height: 220px; }

  .seal {
    position: absolute; border-radius: 50%;
    background: var(--badge);
    border: 4px solid var(--badge-ring);
  }
  .box-front .seal { right: 40px; top: 50px; width: 104px; height: 104px; }
  .bottle-label .seal { right: 40px; top: 34px; width: 66px; height: 66px; border-width: 3px; }

  .brand {
    position: absolute; left: 0; right: 0; text-align: center;
    font-weight: 500; color: var(--ink); letter-spacing: .32em;
  }
  .box-front .brand { top: 205px; font-size: 20px; }
  .bottle-label .brand { top: 110px; font-size: 20px; }

  .strength {
    position: absolute; left: 0; right: 0; text-align: center;
    font-weight: 500; color: var(--ink); letter-spacing: .38em;
  }
  .box-front .strength { top: 318px; font-size: 20px; }
  .bottle-label .strength { top: 188px; font-size: 20px; }

  .product-band {
    position: absolute; left: 0; right: 0;
    background: var(--band);
    border-top: 3px solid var(--rule);
    border-bottom: 3px solid var(--rule);
    color: #fff; text-align: center; font-weight: 500;
  }
  .box-front .product-band { top: 360px; height: 96px; font-size: 50px; line-height: 88px; }
  .bottle-label .product-band { top: 228px; height: 90px; font-size: 50px; line-height: 84px; }

  .subtitle {
    position: absolute; left: 0; right: 0; text-align: center;
    color: #fff; font-weight: 500; letter-spacing: .12em;
  }
  .box-front .subtitle { top: 476px; font-size: 14px; }
  .bottle-label .subtitle { top: 336px; font-size: 14px; }

  .product-icon {
    position: absolute; left: 50%; transform: translateX(-50%);
    background: linear-gradient(135deg, var(--yellow), #f6f6f6);
    border-radius: 14px;
  }
  .box-front .product-icon { top: 525px; width: 100px; height: 80px; }
  .bottle-label .product-icon { top: 370px; width: 80px; height: 56px; }

  .claims {
    position: absolute; left: 0; right: 0; text-align: center;
    font-family: "Roboto Condensed", sans-serif; color: #fff;
    text-transform: uppercase;
  }
  .box-front .claims { top: 625px; font-size: 19px; line-height: 1.5; }
  .bottle-label .claims { top: 440px; font-size: 15px; line-height: 1.5; font-family: "Montserrat", sans-serif; }

  .meta {
    position: absolute; left: 24px; right: 24px;
    display: flex; justify-content: space-between; align-items: baseline;
    color: #fff; text-transform: uppercase; line-height: 1;
    font-family: "Roboto Condensed", sans-serif;
  }
  .box-front .meta { bottom: 48px; font-size: 17px; }
  .bottle-label .meta { bottom: 36px; font-size: 14px; }
  .meta__count { color: var(--yellow); font-size: 2.2em; font-weight: 400; margin-right: 6px; }

  .panel__foot {
    position: absolute; left: 0; right: 0; bottom: 0;
    background: linear-gradient(#eeeeee, var(--silver));
  }
  .box-front .panel__foot { height: 34px; }
  .bottle-label .panel__foot { height: 24px; }
</style>
</head>
<body>

  <section class="panel box-front" aria-label="Box front panel">
    <div class="panel__top"></div>
    <div class="seal" role="img" aria-label="Third party tested badge"></div>
    <p class="brand">TORVESK NUTRITION</p>
    <p class="strength">ULTRA STRENGHTS</p>
    <h1 class="product-band">MULTI VITAMIN</h1>
    <p class="subtitle">30+ WHOLE FOOD FRUITS &amp; VEGETABLE</p>
    <div class="product-icon" role="img" aria-label="Capsule and leaf product icon"></div>
    <p class="claims">Potent energizer &amp; antioxident<br>Performance enhancer<br>Advanced daily multi vitamin complex</p>
    <div class="meta">
      <span><span class="meta__count">180</span>Capsules</span>
      <span>Dietary supllement</span>
    </div>
    <div class="panel__foot"></div>
  </section>

  <section class="panel bottle-label" aria-label="Bottle label">
    <div class="panel__top"></div>
    <div class="seal" role="img" aria-label="Third party tested badge"></div>
    <p class="brand">TORVESK NUTRITION</p>
    <p class="strength">ULTRA STRENGHTS</p>
    <h2 class="product-band">MULTI VITAMIN</h2>
    <p class="subtitle">30+ WHOLE FOOD FRUITS &amp; VEGETABLE</p>
    <div class="product-icon" role="img" aria-label="Capsule and leaf product icon"></div>
    <p class="claims">Potent energizer &amp; antioxident<br>Performance enhancer<br>Advanced daily multi vitamin complex</p>
    <div class="meta">
      <span><span class="meta__count">180</span>Capsules</span>
      <span>Dietary supllement</span>
    </div>
    <div class="panel__foot"></div>
  </section>

</body>
</html>
```